Property Management business needs Business cards designed

We provide a premium property management service based in Sydney's Norther Beaches. We want people to feel confident in choosing us to manage their investment properties. We offer a much more personalized service than other estate agents.
We want a modern clean design. Something that shows confidence without being complicated.
Logo attached.

Target Market(s)

35-70yo Male and Female with strong property portfolios within Sydney's Norther Beaches

Industry/Entity Type

Property Management

Contact Information for Business Card

Address: Suite 7, 12-14 Kelvin Parade, Harlow NSW 2188
Two separate named cards.
Tom Ardley - 0491 570 118 tom@harbourvaleestates.com.au
Clara Dunmore - 0491 570 263 clara@harbourvaleestates.com.au

Requirements
Must have
• Business logo, name, number, address, email.

```html
<!DOCTYPE html>
<html lang="en">
<head>
<meta charset="utf-8">
<title>Harbourvale Estates – Business Cards</title>
<link rel="stylesheet" href="https://fonts.googleapis.com/css2?family=Oswald:wght@400;500;600&family=Noto+Serif:wght@400&display=swap">
<style>
  :root {
    --page: #e9e9e7;
    --card-dark: #16181a;
    --card-dark-2: #2b2e31;
    --card-light: #ffffff;
    --teal: #1a7f8c;
    --teal-line: #2a9fae;
    --ink: #1b1b1b;
    --white: #ffffff;
    --soft: #dfe3e6;
  }
  * { margin: 0; padding: 0; box-sizing: border-box; }
  html, body {
    width: 1200px; height: 902px; overflow: hidden;
    background: var(--page);
  }
  .card {
    position: absolute; left: 240px;
    width: 720px; height: 412px;
    border-radius: 22px; overflow: hidden;
    background: var(--card-light);
    box-shadow: 0 8px 24px rgba(0,0,0,0.16);
  }
  .card--tom { top: 27px; }
  .card--clara { top: 463px; }

  .address-band {
    position: absolute; left: 0; right: 0; top: 244px; height: 70px;
    background: var(--teal);
  }
  .address {
    position: absolute; left: 472px; top: 257px;
    font-family: "Oswald", sans-serif; font-weight: 400;
    font-size: 17px; line-height: 22px; letter-spacing: 0.4px;
    color: var(--white); text-transform: uppercase; white-space: nowrap;
  }
  .brand {
    position: absolute; left: 460px; top: 116px;
    display: flex; align-items: center; gap: 10px;
  }
  .brand-dot {
    width: 16px; height: 16px; border-radius: 50%; flex: none;
    background: var(--teal);
  }
  .brand-name {
    font-family: "Oswald", sans-serif; font-weight: 600;
    font-size: 21px; letter-spacing: 0.4px; white-space: nowrap;
    color: var(--ink); text-transform: uppercase;
  }

  .dark-side {
    position: absolute; inset: 0;
    clip-path: polygon(0 0, 56% 0, 63% 100%, 0 100%);
    background: linear-gradient(100deg, var(--card-dark) 0%, var(--card-dark-2) 48%, var(--card-dark) 75%);
  }
  .accent-line { position: absolute; left: 0; top: 0; }
  .name {
    position: absolute; left: 44px; top: 66px;
    font-family: "Oswald", sans-serif; font-weight: 600;
    font-size: 26px; line-height: 34px; letter-spacing: 1px;
    color: var(--white); text-transform: uppercase; white-space: nowrap;
  }
  .role {
    position: absolute; left: 44px; top: 102px;
    font-family: "Oswald", sans-serif; font-weight: 500;
    font-size: 14px; line-height: 18px; letter-spacing: 1px;
    color: var(--white); text-transform: uppercase;
  }
  .contact {
    position: absolute; left: 56px;
    display: flex; align-items: center; gap: 16px;
  }
  .contact--phone { top: 212px; }
  .contact--email { top: 284px; }
  .contact-icon { width: 30px; height: 30px; flex: none; }
  .contact-text {
    font-family: "Noto Serif", serif; font-weight: 400;
    font-size: 17px; line-height: 24px; color: var(--soft); white-space: nowrap;
  }
</style>
</head>
<body>

  <article class="card card--tom">
    <div class="address-band"></div>
    <p class="address">Suite 7, 12-14 Kelvin Parade,<br>Harlow NSW 2188</p>
    <div class="brand">
      <span class="brand-dot"></span>
      <span class="brand-name">Harbourvale Estates</span>
    </div>
    <section class="dark-side">
      <svg class="accent-line" width="420" height="200" viewBox="0 0 420 200" aria-hidden="true">
        <line x1="0" y1="156" x2="292" y2="98" stroke="var(--teal-line)" stroke-width="1.2"/>
        <circle cx="302" cy="96" r="10" fill="none" stroke="var(--teal-line)" stroke-width="1.6"/>
      </svg>
      <h1 class="name">Tom Ardley</h1>
      <p class="role">( Investor )</p>
      <div class="contact contact--phone">
        <svg class="contact-icon" viewBox="0 0 40 40" aria-hidden="true">
          <circle cx="20" cy="20" r="18" fill="none" stroke="var(--teal-line)" stroke-width="2"/>
          <path d="M14 12c1-1 2-1 3 0l2 3c.5 1 .3 1.7-.5 2.4l-1 .8c.8 2 2.4 3.6 4.4 4.4l.8-1c.7-.8 1.4-1 2.4-.5l3 2c1 1 1 2 0 3l-1.4 1.4c-1.2 1.2-3.2 1.2-5.4 0-3.6-2-6.4-4.8-8.4-8.4-1.2-2.2-1.2-4.2 0-5.4z" fill="var(--white)"/>
        </svg>
        <p class="contact-text">0491 570 118</p>
      </div>
      <div class="contact contact--email">
        <svg class="contact-icon" viewBox="0 0 40 40" aria-hidden="true">
          <circle cx="20" cy="20" r="18" fill="none" stroke="var(--teal-line)" stroke-width="2"/>
          <rect x="11" y="14" width="18" height="12" fill="var(--white)"/>
          <path d="M11 14l9 7 9-7" fill="none" stroke="var(--card-dark)" stroke-width="1.4"/>
        </svg>
        <p class="contact-text">tom@harbourvaleestates.com.au</p>
      </div>
    </section>
  </article>

  <article class="card card--clara">
    <div class="address-band"></div>
    <p class="address">Suite 7, 12-14 Kelvin Parade,<br>Harlow NSW 2188</p>
    <div class="brand">
      <span class="brand-dot"></span>
      <span class="brand-name">Harbourvale Estates</span>
    </div>
    <section class="dark-side">
      <svg class="accent-line" width="420" height="200" viewBox="0 0 420 200" aria-hidden="true">
        <line x1="0" y1="156" x2="292" y2="98" stroke="var(--teal-line)" stroke-width="1.2"/>
        <circle cx="302" cy="96" r="10" fill="none" stroke="var(--teal-line)" stroke-width="1.6"/>
      </svg>
      <h1 class="name">Clara Dunmore</h1>
      <p class="role">( Investor )</p>
      <div class="contact contact--phone">
        <svg class="contact-icon" viewBox="0 0 40 40" aria-hidden="true">
          <circle cx="20" cy="20" r="18" fill="none" stroke="var(--teal-line)" stroke-width="2"/>
          <path d="M14 12c1-1 2-1 3 0l2 3c.5 1 .3 1.7-.5 2.4l-1 .8c.8 2 2.4 3.6 4.4 4.4l.8-1c.7-.8 1.4-1 2.4-.5l3 2c1 1 1 2 0 3l-1.4 1.4c-1.2 1.2-3.2 1.2-5.4 0-3.6-2-6.4-4.8-8.4-8.4-1.2-2.2-1.2-4.2 0-5.4z" fill="var(--white)"/>
        </svg>
        <p class="contact-text">0491 570 263</p>
      </div>
      <div class="contact contact--email">
        <svg class="contact-icon" viewBox="0 0 40 40" aria-hidden="true">
          <circle cx="20" cy="20" r="18" fill="none" stroke="var(--teal-line)" stroke-width="2"/>
          <rect x="11" y="14" width="18" height="12" fill="var(--white)"/>
          <path d="M11 14l9 7 9-7" fill="none" stroke="var(--card-dark)" stroke-width="1.4"/>
        </svg>
        <p class="contact-text">clara@harbourvaleestates.com.au</p>
      </div>
    </section>
  </article>

</body>
</html>
```